Tidewell Cruises. Discover the Coral Coast If You Can

Hello,
I have a catamaran charter business in the Whitsunday Islands, Australia.
My business is called Tidewell Cruises and my catamaran is a Mariner 380 K4 and his name is Quiet Drifter. I have attached its logo but would like something for Tidewell Cruises.
I am looking for a website for my business.
I'm also after 1 logos (for Tidewell Cruises).
I would like to be able to edit the website if needed (putting photos into the gallery, post reviews) and I'll need a shopping cart and all the usual social media contacts.
I will also need a live availability calendar for people to look at to see if the dates they want are available. I will need to easily edit this.
It must also stand out. I can supply most of the picture and maybe some video.
There will only be about 7 pages -
Home - Pictures scrolling past
Price and Availability - Have to show a live calendar that people can click on to see if the dates they want are available.
Gallery - I will put up photos and comments from past charterers.
Contact - A form they fill out to ask questions
Testimonials & Reviews - People can submit photos and review. I will have to be able to easily edit them.
Bookings & Store - If they want to pay by card, or if they want to buy any merchandise and so it would need a shopping cart.
Misc Page - What to bring, What to expect, etc etc
At the moment I only have 1 catamaran that will be advertised but I may get another at a later date.
The site will need a chilled out feel as people will be coming to the Whitsundays to relax and sail around.
The font needs to be a friendly font if this is possible.
The photo I uploaded called Gull Sketch is the logo I want for Tidewell Cruises.
Hope this helps.
Does this sound do-able

Target Market(s)

20 - 60

Industry/Entity Type

Tourism

Coding

Coded - Design and coding required

Number of Pages Required

5+ page

Colors

Designer to choose colors to be used in the design.

Requirements
Must have
• Chilled out feel

```html
<!DOCTYPE html>
<html lang="en">
<head>
<meta charset="utf-8">
<title>Tidewell Cruises — Quiet Drifter</title>
<link rel="stylesheet" href="https://fonts.googleapis.com/css2?family=Montserrat:wght@400;500;600;700&family=Open+Sans:wght@400;600&family=Great+Vibes&display=swap">
<style>
:root{
  --orange:#ef6a2a;
  --orange-dark:#d9541a;
  --ink:#2b2b2b;
  --muted:#707070;
  --navy:#1d3e63;
  --sea:#2b8ea3;
  --sea-deep:#16566b;
  --paper:#ffffff;
  --mist:#f1f1f1;
  --beige:#efe7de;
  --booked:#d2232a;
  --open:#3a9b35;
  --charcoal:#2f2f2f;
}
*{box-sizing:border-box;margin:0;padding:0}
html,body{width:1200px;height:5085px;overflow:hidden}
body{font-family:"Open Sans",Arial,sans-serif;color:var(--ink);background:var(--paper);position:relative}
.abs{position:absolute}
.btn{display:inline-flex;align-items:center;justify-content:center;font-family:"Montserrat",Arial,sans-serif;font-weight:700;font-size:14px;text-transform:uppercase;color:#fff;background:var(--orange);border-radius:22px;letter-spacing:.5px}
.ph{position:absolute}
.heading{font-family:"Montserrat",Arial,sans-serif;font-weight:700;text-transform:uppercase;letter-spacing:1px}
.center{left:0;right:0;text-align:center}

/* header */
.site-header{position:absolute;top:0;left:0;width:1200px;height:102px;background:#fff;border-top:5px solid var(--orange)}
.brand{position:absolute;left:85px;top:22px;display:flex;align-items:center;gap:12px;font-family:"Montserrat",Arial,sans-serif;font-weight:600;font-size:28px;color:var(--orange)}
.brand-dot{width:30px;height:30px;border-radius:50%;background:var(--orange)}
.call{position:absolute;left:740px;top:24px;font-size:14px;color:var(--ink);display:flex;gap:8px;align-items:center}
.book-now{position:absolute;left:973px;top:14px;width:139px;height:38px;border-radius:4px;font-size:15px}
.main-nav{position:absolute;left:370px;top:72px;display:flex;gap:22px;font-family:"Montserrat",Arial,sans-serif;font-size:12px;font-weight:600;text-transform:uppercase;color:var(--ink)}
.main-nav .active{color:var(--orange)}

/* hero */
.hero{position:absolute;top:102px;left:0;width:1200px;height:628px;overflow:hidden;background:#fff}
.hero-photo{left:0;top:0;width:1200px;height:560px;background:radial-gradient(ellipse at 60% 45%,#4fb9c6 0%,#2a8ea6 40%,#145f7a 75%,#0f4660 100%)}
.hero-title{left:90px;width:440px;top:235px;text-align:center;font-family:"Great Vibes",cursive;font-size:84px;color:#fff;line-height:1}
.hero-sub{left:90px;width:440px;top:355px;text-align:center;font-size:15px;color:#fff}
.hero-cta{left:230px;top:406px;width:136px;height:38px;border:2px solid #fff;border-radius:20px;background:transparent;font-size:13px}
.hero-arrow{top:276px;width:34px;height:34px;border-radius:50%;background:rgba(255,255,255,.85)}
.hero-pause{left:560px;top:254px;width:74px;height:74px;border-radius:50%;background:rgba(255,255,255,.45)}
.hero-wave{left:0;top:440px}

/* welcome */
.welcome{position:absolute;top:730px;left:0;width:1200px;height:473px}
.boat-plan{left:61px;top:100px;width:542px;height:255px;background:linear-gradient(180deg,#f5f5f5,#e4e1dc);border-radius:6px}
.welcome-kicker{left:661px;top:105px;font-family:"Montserrat",Arial,sans-serif;font-size:22px;color:var(--orange);text-transform:uppercase;letter-spacing:1px}
.welcome-title{left:661px;top:136px;font-size:42px;color:var(--ink)}
.welcome-text{left:661px;top:197px;width:460px;font-size:13px;line-height:26px;color:var(--muted)}
.welcome-btn{left:661px;top:368px;width:146px;height:42px}

/* availability calendar */
.availability{position:absolute;top:1203px;left:0;width:1200px;height:549px;background:var(--mist)}
.cal-photo{left:102px;top:68px;width:359px;height:417px;background:linear-gradient(180deg,#f6b35c 0%,#e56f2b 45%,#6f3b2a 75%,#2a2220 100%)}
.calendar{left:461px;top:68px;width:641px;height:417px;background:#fff}
.cal-head{height:38px;background:var(--orange);color:#fff;font-family:"Montserrat",Arial,sans-serif;font-weight:600;font-size:17px;display:flex;align-items:center;justify-content:space-between;padding:0 20px}
.cal-grid{width:100%;border-collapse:collapse;table-layout:fixed}
.cal-grid th{height:41px;font-family:"Montserrat",Arial,sans-serif;font-size:13px;font-weight:700;border:1px solid #e3ddd5}
.cal-grid td{height:56px;border:1px solid #e3ddd5;text-align:center;font-size:14px;color:#555;vertical-align:middle}
.cal-grid td.alt{background:var(--beige)}
.tag{display:block;font-size:10px;font-weight:600;text-transform:uppercase;line-height:14px}
.tag.booked{color:var(--booked)}
.tag.open{color:var(--open)}

/* gallery */
.gallery{position:absolute;top:1752px;left:0;width:1200px;height:621px}
.section-title{font-family:"Montserrat",Arial,sans-serif;font-weight:600;text-transform:uppercase;font-size:28px;color:var(--orange);letter-spacing:1px}
.section-sub{font-size:12px;color:var(--muted)}
.g-feature{left:85px;top:129px;width:508px;height:211px;background:var(--orange);color:#fff;text-align:center;padding:60px 50px 0}
.g-feature h3{font-family:"Montserrat",Arial,sans-serif;font-weight:600;font-size:18px;text-transform:uppercase;margin-bottom:12px}
.g-feature p{font-size:12px;line-height:20px}

/* contact */
.contact{position:absolute;top:2373px;left:0;width:1200px;height:637px;background:linear-gradient(180deg,#1c6f8d 0%,#2586a0 35%,#1e5f6f 65%,#28413f 100%)}
.contact-title{top:110px;font-size:30px;color:#fff}
.contact-text{top:170px;left:210px;width:780px;text-align:center;color:#e8f3f6;font-size:12px;line-height:24px}
.field{position:absolute;background:#fff;font-size:12px;color:#555;padding:10px 8px}
.submit{left:542px;top:485px;width:119px;height:40px}

/* testimonials */
.testimonials{position:absolute;top:3010px;left:0;width:1200px;height:475px;background:linear-gradient(180deg,#3b433c 0%,#57604f 50%,#3e4237 100%)}
.testimonials-title{top:78px;font-size:36px;color:#fff;font-weight:600}
.review{position:absolute;top:193px;width:305px;height:204px;border:2px solid #fff;color:#fff;text-align:center;padding:76px 22px 0}
.review p{font-size:12px;font-style:italic;line-height:19px}
.review h4{font-family:"Montserrat",Arial,sans-serif;font-weight:600;font-size:17px;margin-top:16px}
.avatar{position:absolute;left:112px;top:-42px;width:80px;height:80px;border-radius:50%;border:3px solid #fff;background:linear-gradient(135deg,#c7a68a,#8d6c55)}
.nav-dot{position:absolute;width:36px;height:36px;border-radius:50%;background:rgba(255,255,255,.7)}

/* store */
.store{position:absolute;top:3485px;left:0;width:1200px;height:488px;background:linear-gradient(180deg,#1c4e7a,#163e66)}
.store-photo{left:119px;top:41px;width:406px;height:406px;border-radius:50%;border:6px solid #fff;background:linear-gradient(160deg,#8aa38a 0%,#dfe3e2 50%,#7d8c86 100%)}
.store-title{left:597px;top:112px;font-size:38px;color:#fff;font-weight:600}
.store-text{left:597px;top:173px;width:500px;color:#dfe8f2;font-size:13px;line-height:24px}
.price{left:597px;top:298px;font-family:"Montserrat",Arial,sans-serif;font-weight:700;color:#fff;font-size:24px}
.shop-btn{left:597px;top:352px;width:149px;height:41px}

/* price */
.pricing{position:absolute;top:3973px;left:0;width:1200px;height:451px}
.voucher{left:366px;top:163px;width:468px;height:237px;border:4px solid var(--orange);background:linear-gradient(135deg,#fbf4e4,#f1e1be)}

/* what to bring */
.bring{position:absolute;top:4424px;left:0;width:1200px;height:288px;background:linear-gradient(180deg,#f07a32,#e8601f)}
.bring-title{top:42px;font-size:30px;color:#fff;font-weight:600}
.bring-text{top:100px;left:250px;width:700px;text-align:center;color:#fff;font-size:12px;line-height:20px}
.bring-btn{left:519px;top:193px;width:159px;height:48px;background:var(--charcoal);border-radius:3px}

/* footer */
.site-footer{position:absolute;top:4712px;left:0;width:1200px;height:373px;background:#fff}
.footer-brand{top:62px;display:flex;justify-content:center;align-items:center;gap:12px;font-family:"Montserrat",Arial,sans-serif;font-weight:600;font-size:34px;color:var(--charcoal)}
.footer-brand .brand-dot{background:var(--orange);width:34px;height:34px}
.rule{position:absolute;left:85px;width:1030px;height:1px;background:#dcdcdc}
.contact-item{position:absolute;top:190px;display:flex;gap:16px;align-items:flex-start}
.icon-ring{width:52px;height:52px;border-radius:50%;border:1px solid #cfcfcf;display:flex;align-items:center;justify-content:center}
.contact-item h5{font-family:"Montserrat",Arial,sans-serif;font-weight:500;font-size:16px;color:var(--ink);margin-bottom:4px}
.contact-item p{font-size:12px;color:var(--muted);line-height:18px}
.copyright{left:85px;top:326px;font-size:12px;color:var(--muted)}
.social{left:875px;top:314px;display:flex;gap:8px}
.social span{width:30px;height:30px;border-radius:50%;background:var(--navy)}
.to-top{left:1128px;top:326px;font-size:12px;color:var(--muted)}
</style>
</head>
<body>

<header class="site-header">
  <div class="brand"><span class="brand-dot"></span>Tidewell Cruises</div>
  <div class="call">
    <svg width="16" height="16" viewBox="0 0 24 24" fill="#ef6a2a"><path d="M6.6 10.8a15 15 0 0 0 6.6 6.6l2.2-2.2a1 1 0 0 1 1-.25 11.4 11.4 0 0 0 3.6.57 1 1 0 0 1 1 1V20a1 1 0 0 1-1 1A17 17 0 0 1 3 4a1 1 0 0 1 1-1h3.5a1 1 0 0 1 1 1c0 1.25.2 2.45.57 3.57a1 1 0 0 1-.25 1z"/></svg>
    Call Us : (+61) 1-800-555-0142
  </div>
  <div class="btn book-now">Book Now</div>
  <nav class="main-nav">
    <span class="active">Home</span><span>Price &amp; Availability</span><span>Gallery</span><span>Contact</span><span>Testimonials &amp; Reviews</span><span>Bookings &amp; Store</span><span>Misc</span>
  </nav>
</header>

<section class="hero">
  <div class="ph hero-photo" role="img" aria-label="Aerial photo of turquoise reef waters around the islands"></div>
  <h1 class="abs hero-title">Quiet Drifter</h1>
  <p class="abs hero-sub">Sail the calm reef waters at your own easy pace</p>
  <div class="abs btn hero-cta">Get Started</div>
  <div class="abs hero-arrow" style="left:41px"><svg width="34" height="34" viewBox="0 0 34 34"><path d="M20 10l-7 7 7 7" fill="none" stroke="#333" stroke-width="2.5"/></svg></div>
  <div class="abs hero-arrow" style="left:1122px"><svg width="34" height="34" viewBox="0 0 34 34"><path d="M14 10l7 7-7 7" fill="none" stroke="#333" stroke-width="2.5"/></svg></div>
  <div class="abs hero-pause"><svg width="74" height="74" viewBox="0 0 74 74"><rect x="28" y="25" width="6" height="24" fill="#fff"/><rect x="40" y="25" width="6" height="24" fill="#fff"/></svg></div>
  <svg class="abs hero-wave" width="1200" height="190" viewBox="0 0 1200 190" preserveAspectRatio="none">
    <path d="M0 30 C300 160 800 170 1200 20 L1200 190 L0 190Z" fill="#ef6a2a"/>
    <path d="M0 80 C330 190 820 180 1200 60 L1200 190 L0 190Z" fill="#fff"/>
    <path d="M0 95 C350 200 820 195 1200 90 L1200 190 L0 190Z" fill="#fff"/>
  </svg>
</section>

<section class="welcome">
  <div class="ph boat-plan" role="img" aria-label="Top-down deck plan drawing of the catamaran"></div>
  <p class="abs welcome-kicker">Welcome to</p>
  <h2 class="abs heading welcome-title">Quiet Drifter</h2>
  <p class="abs welcome-text">Step aboard our roomy catamaran and let the islands set the pace. Spacious cabins, a shaded deck and a friendly crew make every day easy. Swim off the back, snorkel the fringing reef, or simply stretch out with a book while the breeze carries you on to the next quiet bay. Relax, unwind and enjoy it all.</p>
  <div class="abs btn welcome-btn">Read More</div>
</section>

<section class="availability">
  <div class="ph cal-photo" role="img" aria-label="Sunset over the water seen from the catamaran deck"></div>
  <div class="abs calendar">
    <div class="cal-head"><span>&#9664;</span><span>MAY 2018</span><span>&#9654;</span></div>
    <table class="cal-grid">
      <thead><tr><th>SUN</th><th>MON</th><th>TUE</th><th>WED</th><th>THU</th><th>FRI</th><th>SAT</th></tr></thead>
      <tbody>
        <tr><td class="alt"></td><td></td><td class="alt"></td><td></td><td class="alt"></td><td></td><td>1</td></tr>
        <tr><td class="alt">2</td><td>3</td><td class="alt">4</td><td>5</td><td class="alt">6</td><td>7</td><td class="alt">8</td></tr>
        <tr><td><span class="tag booked">Booked</span>9</td><td class="alt">10</td><td><span class="tag open">&#10004; Available</span>11</td><td class="alt">12</td><td>13</td><td class="alt"><span class="tag booked">Booked</span>14</td><td>15</td></tr>
        <tr><td class="alt"><span class="tag open">&#10004; Available</span>16</td><td>17</td><td class="alt">18</td><td><span class="tag booked">Booked</span>19</td><td class="alt">20</td><td><span class="tag open">&#10004; Available</span>21</td><td class="alt">22</td></tr>
        <tr><td>23</td><td class="alt"><span class="tag booked">Booked</span>24</td><td>25</td><td class="alt"><span class="tag open">&#10004; Available</span>26</td><td>27</td><td class="alt">28</td><td>29</td></tr>
        <tr><td class="alt">30</td><td>31</td><td class="alt"></td><td></td><td class="alt"></td><td></td><td class="alt"></td></tr>
      </tbody>
    </table>
  </div>
</section>

<section class="gallery">
  <h2 class="abs center section-title" style="top:42px">Photo Gallery</h2>
  <p class="abs center section-sub" style="top:86px">Moments shared by our guests from sunny days on the reef and calm nights at anchor</p>
  <div class="ph g-feature">
    <h3>Life on the water</h3>
    <p>Fresh photos from recent charters, added after every trip.<br>Tap any image to see the story behind it.</p>
  </div>
  <div class="ph" style="left:603px;top:129px;width:251px;height:434px;background:linear-gradient(180deg,#f2a654,#b5532a 55%,#2d2522)" role="img" aria-label="Sunset view from the deck"></div>
  <div class="ph" style="left:864px;top:129px;width:248px;height:211px;background:linear-gradient(160deg,#2c6f84,#0f3d4f)" role="img" aria-label="Underwater coral close-up"></div>
  <div class="ph" style="left:85px;top:350px;width:250px;height:213px;background:linear-gradient(180deg,#b9d3df,#5e8aa0 60%,#2a4a66)" role="img" aria-label="Inflatable tender on calm water"></div>
  <div class="ph" style="left:346px;top:350px;width:247px;height:213px;background:linear-gradient(180deg,#3f9ab0,#1f5f72 60%,#5c6b4a)" role="img" aria-label="Snorkeller above the reef"></div>
  <div class="ph" style="left:864px;top:350px;width:248px;height:213px;background:linear-gradient(160deg,#2e7f6b,#7a9b4a 50%,#c33f7a)" role="img" aria-label="Flowering shrubs on the shoreline"></div>
</section>

<section class="contact">
  <div class="ph" style="inset:0" role="img" aria-label="Underwater scene with coral and a diver"></div>
  <h2 class="abs center heading contact-title" style="font-weight:600">Contact Us</h2>
  <p class="abs contact-text">Have a question about dates, cabins or what to pack? Send us a note and we will reply within a day. We are always happy to help plan the perfect trip for your group.</p>
  <div class="field" style="left:220px;top:264px;width:373px;height:38px">First Name</div>
  <div class="field" style="left:610px;top:264px;width:373px;height:38px">Last Name</div>
  <div class="field" style="left:220px;top:329px;width:373px;height:38px">Email</div>
  <div class="field" style="left:610px;top:329px;width:373px;height:38px">Subject</div>
  <div class="field" style="left:220px;top:393px;width:763px;height:64px">Message</div>
  <div class="abs btn submit">Submit</div>
</section>

<section class="testimonials">
  <h2 class="abs center heading testimonials-title">Testimonials &amp; Reviews</h2>
  <div class="nav-dot" style="left:34px;top:277px"><svg width="36" height="36" viewBox="0 0 36 36"><path d="M21 11l-7 7 7 7" fill="none" stroke="#333" stroke-width="2.5"/></svg></div>
  <div class="nav-dot" style="left:1130px;top:277px"><svg width="36" height="36" viewBox="0 0 36 36"><path d="M15 11l7 7-7 7" fill="none" stroke="#333" stroke-width="2.5"/></svg></div>
  <div class="review" style="left:102px"><div class="avatar" role="img" aria-label="Guest portrait"></div><p>Best week of our year, calm seas and a crew who thought of everything for us.</p><h4>Nora Bellamy</h4></div>
  <div class="review" style="left:444px"><div class="avatar" role="img" aria-label="Guest portrait"></div><p>We swam with turtles every morning and watched sunsets every night. Pure bliss.</p><h4>Jess Whitcombe</h4></div>
  <div class="review" style="left:793px"><div class="avatar" role="img" aria-label="Guest portrait"></div><p>Comfortable boat, friendly skipper and the clearest water we have ever seen.</p><h4>Owen Raddle</h4></div>
</section>

<section class="store">
  <svg class="abs" style="left:38px;top:215px" width="24" height="60" viewBox="0 0 24 60"><path d="M20 2L4 30l16 28" fill="none" stroke="#fff" stroke-width="2"/></svg>
  <svg class="abs" style="left:1138px;top:215px" width="24" height="60" viewBox="0 0 24 60"><path d="M4 2l16 28L4 58" fill="none" stroke="#fff" stroke-width="2"/></svg>
  <div class="ph store-photo" role="img" aria-label="Crew T-shirt product photo"></div>
  <h2 class="abs heading store-title">Our Store</h2>
  <p class="abs store-text">Take a little piece of the islands home. Soft cotton crew tees, caps and water bottles, all printed locally and shipped anywhere in Australia within a week.</p>
  <p class="abs price">$20.00</p>
  <div class="abs btn shop-btn">Shop Now</div>
</section>

<section class="pricing">
  <h2 class="abs center section-title" style="top:34px">Availability &amp; Price</h2>
  <p class="abs center section-sub" style="top:80px;left:250px;right:250px;line-height:22px">Charters run year round with weekly and short-stay options. Gift vouchers make a perfect present for anyone who loves the sea.</p>
  <div class="ph voucher" role="img" aria-label="Gift voucher card for a charter"></div>
</section>

<section class="bring">
  <h2 class="abs center heading bring-title">What to Bring, What to Expect</h2>
  <p class="abs bring-text">Pack light: swimwear, a hat, reef-safe sunscreen and soft-soled shoes. Linen, snorkel gear and meals are provided on board. Expect gentle sailing, quiet anchorages and plenty of time to simply do nothing at all.</p>
  <div class="abs btn bring-btn">Read More</div>
</section>

<footer class="site-footer">
  <div class="rule" style="top:1px"></div>
  <div class="abs center footer-brand"><span class="brand-dot"></span>Tidewell Cruises</div>
  <div class="rule" style="top:165px"></div>
  <div class="contact-item" style="left:119px">
    <div class="icon-ring"><svg width="20" height="20" viewBox="0 0 24 24" fill="#555"><path d="M12 2a7 7 0 0 0-7 7c0 5 7 13 7 13s7-8 7-13a7 7 0 0 0-7-7zm0 9.5A2.5 2.5 0 1 1 12 6.5a2.5 2.5 0 0 1 0 5z"/></svg></div>
    <div><h5>Address :</h5><p>12 Marina Parade, Harbour Point<br>Coral Coast QLD</p></div>
  </div>
  <div class="contact-item" style="left:525px">
    <div class="icon-ring"><svg width="20" height="20" viewBox="0 0 24 24" fill="none" stroke="#555" stroke-width="2"><rect x="3" y="5" width="18" height="14" rx="1"/><path d="M3 6l9 7 9-7"/></svg></div>
    <div><h5>Email</h5><p>hello@tidewellcruises.example</p></div>
  </div>
  <div class="contact-item" style="left:888px">
    <div class="icon-ring"><svg width="20" height="20" viewBox="0 0 24 24" fill="#555"><path d="M6.6 10.8a15 15 0 0 0 6.6 6.6l2.2-2.2a1 1 0 0 1 1-.25 11.4 11.4 0 0 0 3.6.57 1 1 0 0 1 1 1V20a1 1 0 0 1-1 1A17 17 0 0 1 3 4a1 1 0 0 1 1-1h3.5a1 1 0 0 1 1 1c0 1.25.2 2.45.57 3.57a1 1 0 0 1-.25 1z"/></svg></div>
    <div><h5>Phone</h5><p>Mobile : (07) 5550 0199</p></div>
  </div>
  <div class="rule" style="top:288px"></div>
  <p class="abs copyright">© Copyright 2018 Quiet Drifter. All rights reserved</p>
  <div class="abs social" aria-label="Social media links"><span></span><span></span><span></span><span></span><span></span><span></span><span></span></div>
  <p class="abs to-top">Top</p>
</footer>

</body>
</html>
```